Psychologist in Private Practice Needs a Website Update

Project Description:
Hello talented designers! My current website, www.jodelbrisk.com, needs a fresh, boho-modern makeover that highlights the warm, welcoming nature of my holistic therapy practice. I want a website that has a serene, boho- modern design, appealing to clients seeking individual therapy, couples therapy, and family counseling.

I’d also like to prepare for a future second site focused exclusively on couples and family therapy. Both sites should be interconnected, so I’m looking for design suggestions that seamlessly link them together while maintaining a cohesive brand look and feel.

Key Objectives:

Boho-Modern Aesthetic: Incorporate natural textures, neutral or earthy tones, and clean lines that capture a modern, inviting vibe.

Responsive Design: Ensure the website is user-friendly on desktop, tablet, and mobile devices.

Clear Service Offerings: Prominently feature my three distinct services: individual therapy, couples therapy, and family counseling.

Interlinked Future Site: Provide ideas on how to cross-link this site with a second site focused on couples and family therapy.

User Experience (UX): Make the site simple to navigate, with intuitive placement of content that speaks to potential clients’ needs.

SEO-Friendly: Implement best practices for structure, site speed, and keyword usage to boost online visibility.

What I Have Now:
Existing website: www.jodelbrisk.com
Basic content and a logo that can be refined or updated to match the boho-modern feel
Rough style guide with brand elements open to a fresh interpretation

Preferred Style/Tone:
Boho-modern with earthy tones, subtle textures, and clean typography
Warm, empathetic, and approachable to align with the nature of therapy services
Slightly artistic or organic elements that evoke calm and connection

Potential for an ongoing design relationship!
Updates

Need extra days to review

Target Market(s)

I have a high functioning, professional clientele who doctors, lawyers, and leaders in their field.

Industry/Entity Type

healthcare/mental health

Coding

Coded - Design and coding required

Font styles to use
Other font styles liked:
• cormorant garamond for headers and Source Sans Pro for supporting text

Colors

Designer to choose colors to be used in the design.

Requirements
Must have
• Open, Harmonious Layout I’d like the overall design to feel upscale, humanistic, open and harmonious, with minimal divisions of space. Rather than traditional section dividers, please consider using images, subtle shifts in color, typography, or spacing to define sections. Hero Image & Inspiration Ideally, the first (hero) image should evoke a sense of awe or inspiration. Focus on simplicity and elegance so the design feels spacious and inviting, allowing the content and imagery to really stand out. Natural Flow Wherever possible, let the design elements flow naturally into each other, creating a sense of unity and cohesion throughout the site.
Nice to have
• 1. Full-Width Hero Image: • The homepage should feature a full-width hero image that extends edge-to-edge across the screen for a modern and visually immersive effect. • This image should set the tone for the website, reflecting a calming, humanistic/natural, and upscale feel. It could include subtle overlays or gradients to enhance readability of text and navigation elements. Ideally, this image should have one or two people in nature. The image could be slightly transparent to allow the text "holistic therapy" and the tagline "an integrative approach to transformation" to be easily visible. Please help me find a breath-taking image that evokes a sense of beauty, inspiration, awe or hope. 2. Menu Tabs Positioned Over the Image: • The menu tabs (navigation bar) should be positioned directly on top of the hero image, either centered or aligned to the top right/left, depending on the design. • The navigation bar should have a slightly transparent or solid background (depending on the image and visibility needs) to ensure the text is easily readable without detracting from the image. 3. Typography and Text Placement: • The text overlay on the hero image should use the selected fonts: • Cormorant Garamond for headers (e.g., the tagline or welcome message). • Source Sans Pro for any supporting text. 5. Seamless Transitions: • Below the full-width image, transitions into the next sections (like “About,” “Services,” or client-focused content) should be smooth, using full-width separators that maintain the cohesive, open layout style. 6. Color Palette: • A neutral and calming color palette should be used (e.g., soft blues, grays, whites, or very muted earth tones) to create a soothing atmosphere for visitors. This design approach ensures the homepage looks clean, modern, and professional while maintaining the calming and upscale aesthetic that reflects the values of my psychology practice

```html
<!DOCTYPE html>
<html lang="en">
<head>
<meta charset="utf-8">
<title>Dr. Jodel Brisk – Mobile Screens</title>
<link href="https://fonts.googleapis.com/css2?family=Poppins:wght@400;500;600;700&display=swap" rel="stylesheet">
<style>
:root{
  --teal:#3a9aad;
  --teal-dark:#2f8497;
  --amber:#e8a512;
  --ink:#1c1c1c;
  --muted:#555;
  --paper:#ffffff;
  --canvas:#f4f4f4;
}
*{box-sizing:border-box;margin:0;padding:0}
html,body{width:1200px;height:503px;overflow:hidden;background:var(--canvas);font-family:"Poppins",sans-serif;color:var(--ink)}
.board{display:flex;gap:14px;padding:14px 10px;height:503px}
.screen{width:185px;height:475px;background:var(--paper);overflow:hidden;border-radius:8px;box-shadow:0 2px 10px rgba(0,0,0,.07);display:flex;flex-direction:column}
.photo{flex:none}
.btn{display:inline-block;background:var(--amber);color:#fff;font-size:6.5px;padding:5px 11px;border-radius:1px}
.h2{font-weight:700;font-size:12px;line-height:1.2;text-align:center}
.h2 span{color:var(--teal)}
.sub{font-size:5.5px;text-align:center;color:var(--muted);margin-top:2px}
.h3{font-weight:700;font-size:9px;text-align:center;margin-top:7px}
.p{font-size:5.8px;line-height:1.55;text-align:center;color:#333;margin:4px 10px 6px}
.center{text-align:center}
/* screen 1 */
.topbar{display:flex;align-items:center;justify-content:space-between;padding:7px 9px;background:#fff}
.brand{display:flex;align-items:center;gap:4px}
.brand-dot{width:9px;height:9px;border-radius:50%;background:var(--teal)}
.brand-name{font-size:6px;font-weight:500;color:var(--teal);line-height:1.1}
.brand-name small{display:block;font-size:4.5px}
.menu{width:12px;height:12px;background:var(--teal);border-radius:1px;display:flex;flex-direction:column;justify-content:center;gap:1.5px;padding:0 3px}
.menu i{height:1px;background:#fff;display:block}
.hero{flex:1;background:linear-gradient(160deg,#9a9a9a,#7a7878 55%,#8d8a86);display:flex;flex-direction:column;justify-content:center;align-items:center;padding:0 12px;text-align:center;color:#fff}
.hero h1{font-size:14px;font-weight:600;line-height:1.55}
.hero h1 span{color:#4fb6c9}
.hero hr{width:100%;border:0;border-top:1px solid rgba(255,255,255,.7);margin:6px 0}
.hero p{font-size:5.8px;line-height:1.6;margin-bottom:10px}
/* frames */
.portrait-wrap{margin:8px 12px;background:var(--teal);padding:10px}
.frame-under{border-bottom:3px solid var(--teal)}
/* about panel */
.care{flex:1;background:linear-gradient(180deg,#c7c1b8 0,#c7c1b8 40px,#b18a64 100%);padding:30px 12px}
.care-box{background:var(--teal);color:#fff;padding:14px 11px;height:100%}
.care-box h3{font-size:10px;font-weight:600;line-height:1.3}
.care-box p{font-size:5.8px;line-height:1.5;margin-top:6px}
.value{display:flex;gap:7px;margin-top:12px}
.value .ic{flex:none;width:13px;height:13px;border-radius:50%;background:rgba(255,255,255,.25)}
.value b{font-size:6.5px;display:block}
.value span{font-size:5.6px;line-height:1.5}
/* testimonial */
.quote{background:var(--teal);color:#fff;margin:-18px 12px 0;position:relative;padding:11px;display:flex;gap:7px}
.quote .av{flex:none;width:16px;height:16px;border-radius:50%;background:#e7ddd4}
.quote p{font-size:5.8px;line-height:1.55}
.quote em{display:block;font-style:normal;margin-top:4px;font-size:6px}
.arrows{display:flex;justify-content:center;gap:5px;margin:7px 0 10px}
.arrows span{width:11px;height:11px;border-radius:50%;background:var(--teal);color:#fff;font-size:6px;display:flex;align-items:center;justify-content:center}
.meta{font-size:4.8px;color:var(--amber);text-align:center}
/* contact */
.cta{position:relative;height:92px;background:linear-gradient(135deg,#cfc9c0,#a9a39b);display:flex;flex-direction:column;justify-content:center;align-items:center;color:#fff;gap:6px}
.cta b{font-size:9px;text-align:center;line-height:1.3}
.info{display:flex;gap:6px;align-items:center;margin:5px 14px;padding-bottom:5px;border-bottom:1px solid #eee}
.info svg{flex:none}
.info b{font-size:6.5px;display:block}
.info span{font-size:5.5px;color:var(--muted)}
.form{background:var(--teal);margin:6px 12px;padding:9px 10px;color:#fff}
.form label{font-size:6px;display:block;margin-top:4px}
.form .field{background:#fff;height:12px;margin-top:2px;font-size:4.8px;color:#999;padding:3px 4px}
.footer{flex:1;background:var(--teal);color:#fff;padding:9px 12px;border-top:4px solid var(--amber)}
.footer b{font-size:6.5px;display:block;margin-top:5px}
.footer span{font-size:5.2px;display:block;line-height:1.5}
</style>
</head>
<body>
<main class="board">

  <!-- Home hero -->
  <section class="screen">
    <header class="topbar">
      <div class="brand"><span class="brand-dot"></span><span class="brand-name">Dr. Jodel Brisk<small>Licensed Psychologist</small></span></div>
      <div class="menu"><i></i><i></i><i></i></div>
    </header>
    <div class="hero" role="img" aria-label="Soft grey photo of a therapist taking notes with a client">
      <h1><span>Experience Holistic</span><br>Healing with a Boho-Modern Touch</h1>
      <hr>
      <p>Transform your life and strengthen your relationships with our personalized approach to individual therapy, couples counseling, and family support.</p>
      <span class="btn">Start Your Journey</span>
    </div>
  </section>

  <!-- About + services start -->
  <section class="screen">
    <p class="p" style="margin-top:12px">Guiding clients with an empathetic presence through life's transitions toward understanding, and peace.</p>
    <div class="center"><span class="btn">Learn More</span></div>
    <div class="portrait-wrap"><div class="photo" role="img" aria-label="Portrait of the psychologist smiling" style="height:100px;background:linear-gradient(160deg,#b58a63,#5e4537)"></div></div>
    <h2 class="h2" style="margin-top:6px">Our Therapy <span>Services</span></h2>
    <p class="sub">Tailored Support for Your Unique Journey</p>
    <div class="photo frame-under" role="img" aria-label="Therapist in session with a young man in a bright room" style="height:88px;margin:8px 12px 0;background:linear-gradient(135deg,#e9e3da,#9fb3c0)"></div>
    <h3 class="h3">Individual Therapy</h3>
    <p class="p">Discover personal growth and clarity in a supportive, one-on-one setting. Our individual therapy sessions are designed to help you navigate life's complexities with compassion and insight.</p>
    <div class="center"><span class="btn">Learn More</span></div>
  </section>

  <!-- Services continued -->
  <section class="screen">
    <div class="photo frame-under" role="img" aria-label="Family talking together on a sofa" style="height:95px;margin:12px 12px 0;background:linear-gradient(135deg,#d8d3cc,#6f6a66)"></div>
    <h3 class="h3">Family Counseling</h3>
    <p class="p">Enhance family dynamics and foster harmony. Our family counseling sessions address various challenges, promoting understanding and unity within your family.</p>
    <div class="center"><span class="btn">Learn More</span></div>
    <div class="photo frame-under" role="img" aria-label="Couple holding hands in a counseling session" style="height:95px;margin:14px 12px 0;background:linear-gradient(135deg,#c9a98a,#4f4a47)"></div>
    <h3 class="h3">Couples Therapy</h3>
    <p class="p">Strengthen your relationship with tailored guidance for couples. Our sessions provide a safe space to improve communication, resolve conflicts, and deepen your connection.</p>
    <div class="center"><span class="btn">Learn More</span></div>
  </section>

  <!-- Compassionate care -->
  <section class="screen">
    <div class="care" role="img" aria-label="Warm interior with a leafy plant and wooden floor">
      <div class="care-box">
        <h3>Compassionate Care from Trusted Professionals</h3>
        <p>At our core, we are committed to providing exceptional care that prioritizes your well-being.</p>
        <div class="value"><span class="ic"></span><div><b>Vision</b><span>To be a beacon of hope and transformation, empowering individuals and families to achieve mental and emotional well-being.</span></div></div>
        <div class="value"><span class="ic"></span><div><b>Mission</b><span>To deliver personalized, high-quality therapy services that foster growth, resilience, and meaningful connections in a supportive and nurturing environment.</span></div></div>
        <div class="value"><span class="ic"></span><div><b>Motto</b><span>Your path to peace, guided by care and compassion.</span></div></div>
      </div>
    </div>
  </section>

  <!-- Testimonial + blog -->
  <section class="screen">
    <h2 class="h2" style="margin-top:10px">Hear From <span>Clients</span></h2>
    <div class="photo" role="img" aria-label="Happy family with a child on the father's shoulders" style="height:120px;margin:8px 12px 0;background:linear-gradient(160deg,#dfe4ea,#8ea3b8)"></div>
    <div class="quote"><span class="av"></span><p>Jodel's compassionate approach has transformed my life. Her guidance has been invaluable in helping me find peace and clarity.<em>— Lena R.</em></p></div>
    <div class="arrows"><span>‹</span><span>›</span></div>
    <h2 class="h2"><span>Insights</span> &amp; Articles</h2>
    <p class="sub">Explore our latest blog posts and articles on wellness, mental health, and personal growth.</p>
    <div class="photo frame-under" role="img" aria-label="Two people embracing on a beach" style="height:92px;margin:8px 12px 0;background:linear-gradient(135deg,#b9c9d3,#8a6a52)"></div>
    <h3 class="h3">5 Mindfulness Techniques for Everyday Calm</h3>
    <p class="p">Discover simple mindfulness exercises to help you stay grounded and calm throughout your day.</p>
    <p class="meta">07 December 2024 · 0 Comments</p>
  </section>

  <!-- Contact + footer -->
  <section class="screen">
    <div class="cta" role="img" aria-label="Parent carrying a smiling child on a balcony, softened">
      <b>Getting better starts<br>with mental health</b>
      <span class="btn">Consultation Now</span>
    </div>
    <h2 class="h2" style="margin-top:8px">We're Here to<br><span>Help You</span></h2>
    <p class="p">Ready to start your healing journey? Reach out to us today to schedule a session or learn more about our services.</p>
    <div class="info"><svg width="12" height="12" viewBox="0 0 12 12"><circle cx="6" cy="6" r="6" fill="#3a9aad"/><path d="M4 3.3l1 1.3-.6.7c.4.9 1.1 1.6 2 2l.7-.6 1.3 1-.6 1c-2.3-.2-4.3-2.2-4.5-4.5z" fill="#fff"/></svg><div><b>Phone Number</b><span>+987 000 1122</span></div></div>
    <div class="info"><svg width="12" height="12" viewBox="0 0 12 12"><circle cx="6" cy="6" r="6" fill="#3a9aad"/><circle cx="6" cy="6" r="3" fill="none" stroke="#fff" stroke-width=".8"/><path d="M6 4.3V6l1.1.8" stroke="#fff" stroke-width=".8" fill="none"/></svg><div><b>Business Hours</b><span>Mon–Fri, 07.00–16.00</span></div></div>
    <div class="info"><svg width="12" height="12" viewBox="0 0 12 12"><circle cx="6" cy="6" r="6" fill="#3a9aad"/><path d="M6 9.3S3.8 6.9 3.8 5.2a2.2 2.2 0 014.4 0C8.2 6.9 6 9.3 6 9.3z" fill="#fff"/><circle cx="6" cy="5.2" r=".8" fill="#3a9aad"/></svg><div><b>Address</b><span>48 Linden Row, Maplebrook</span></div></div>
    <div class="form">
      <label>Your Name</label><div class="field">Enter your name</div>
      <label>Your Email</label><div class="field">Enter your email</div>
      <div style="margin-top:6px"><span class="btn">Send Message</span></div>
    </div>
    <footer class="footer">
      <b>Contact</b>
      <span>12 Willow Lane, Fernvale · (123) 000-4455</span>
      <span>hello@jodelbrisk.com · www.jodelbrisk.com</span>
      <b>Navigation</b>
      <span>Home · About Us · Our Services · Blog · Contact Us</span>
    </footer>
  </section>

</main>
</body>
</html>
```